VAN WRAP

I would like to have my logo for my electrical contracting company on my 2018 kestrel haulmax 300 lab short roof. I do like the white front and black back. The business is located st George Utah. web site is www.harvelelectrical.us and phone number is 4355550182.

```html
<!DOCTYPE html>
<html lang="en">
<head>
<meta charset="utf-8">
<title>Harvel Electrical Contractors – Van Wrap</title>
<link rel="stylesheet" href="https://fonts.googleapis.com/css2?family=Russo+One&family=Montserrat:wght@500&family=Roboto:wght@500;700&display=swap">
<style>
  :root {
    --wrap-white: #ffffff;
    --ink: #1c1c1c;
    --brand-red: #e8262b;
    --pattern-pink: #f29c9d;
    --pattern-pink-soft: #f8cfcf;
    --band-black: #2b2b2b;
  }
  html, body {
    margin: 0;
    padding: 0;
    overflow: hidden;
    background: var(--wrap-white);
  }
  .wrap-side {
    position: relative;
    width: 1200px;
    height: 617px;
    overflow: hidden;
    background: var(--wrap-white);
  }
  .wrap-art {
    position: absolute;
    inset: 0;
  }
  .brand-square {
    position: absolute;
    left: 560px;
    top: 184px;
    width: 70px;
    height: 70px;
    background: var(--brand-red);
  }
  .brand-name {
    margin: 0;
    font-weight: 400;
    color: var(--ink);
  }
  .brand-name-main {
    position: absolute;
    left: 646px;
    top: 166px;
    font-family: "Russo One", sans-serif;
    font-size: 80px;
    line-height: 1;
    letter-spacing: 3px;
  }
  .brand-name-sub {
    position: absolute;
    left: 650px;
    top: 247px;
    font-family: "Montserrat", sans-serif;
    font-weight: 500;
    font-size: 15px;
    line-height: 1;
    letter-spacing: 6.4px;
    white-space: nowrap;
  }
  .contact {
    position: absolute;
    left: 252px;
    top: 308px;
    font-family: "Roboto", sans-serif;
  }
  .contact-phone {
    display: flex;
    align-items: center;
    gap: 4px;
    font-size: 28px;
    font-weight: 700;
    line-height: 1.1;
    color: var(--ink);
    letter-spacing: 1px;
  }
  .contact-phone svg {
    width: 22px;
    height: 22px;
  }
  .contact-web {
    margin: 2px 0 0 38px;
    font-size: 17px;
    font-weight: 500;
    color: var(--brand-red);
  }
</style>
</head>
<body>
  <main class="wrap-side">
    <svg class="wrap-art" width="1200" height="617" viewBox="0 0 1200 617">
      <defs>
        <linearGradient id="pattern-fade" x1="0" y1="1" x2="1" y2="0">
          <stop offset="0" stop-color="var(--pattern-pink-soft)"/>
          <stop offset="0.45" stop-color="var(--pattern-pink)"/>
          <stop offset="1" stop-color="var(--pattern-pink)"/>
        </linearGradient>
      </defs>
      <path class="pattern-field-upper" role="img" aria-label="Red diamond tile pattern sweeping up toward the rear of the van"
        fill="url(#pattern-fade)"
        d="M598,377 L628,356 L652,350 L676,326 L700,316 L720,300 L748,290 L770,272 L800,268 L830,246
           L870,238 L905,214 L940,206 L975,184 L1010,176 L1040,156 L1070,150 L1100,122 L1116,130
           L1116,377 Z"/>
      <rect class="lower-band" x="60" y="377" width="1080" height="54" fill="var(--band-black)"/>
      <path class="pattern-field-lower" role="img" aria-label="Red diamond tile pattern along the rocker strip"
        fill="url(#pattern-fade)"
        d="M396,462 L420,446 L450,446 L470,434 L810,434 L810,462 Z"/>
      <rect class="rocker-edge" x="330" y="462" width="490" height="8" fill="var(--band-black)"/>
    </svg>

    <div class="brand-square"></div>
    <h1 class="brand-name">
      <span class="brand-name-main">HARVEL</span>
      <span class="brand-name-sub">ELECTRICAL CONTRACTORS</span>
    </h1>

    <div class="contact">
      <div class="contact-phone">
        <svg viewBox="0 0 24 24" aria-hidden="true">
          <path fill="var(--brand-red)" d="M6.6 10.8a15.1 15.1 0 0 0 6.6 6.6l2.2-2.2a1 1 0 0 1 1-.25 11.4 11.4 0 0 0 3.6.57 1 1 0 0 1 1 1V20a1 1 0 0 1-1 1A17 17 0 0 1 3 4a1 1 0 0 1 1-1h3.5a1 1 0 0 1 1 1c0 1.25.2 2.45.57 3.57a1 1 0 0 1-.25 1z"/>
          <path fill="none" stroke="var(--brand-red)" stroke-width="1.8" stroke-linecap="round" d="M14.5 3.5a6 6 0 0 1 6 6M14.5 7a2.5 2.5 0 0 1 2.5 2.5"/>
        </svg>
        <span>4355550182</span>
      </div>
      <div class="contact-web">harvelelectrical.us</div>
    </div>
  </main>
</body>
</html>
```